Established Mortgage Brokerage Needs Wordpress Site for Corporate website

We need a wordpress website designed for a well-established Mortgage Brokerage in Oakville, Ontario. Our firm provides residential and commercial mortgage solutions for clients in Ontario, Canada. The final design should communicate professionalism, reliability, trustworthiness, financial stability. Colour scheme should be in line with our logo per attached files.

Target Market(s)

End consumer is knowledgable. Will vary from working families to business professionals, looking for financing alternatives for various types of real estate.

Other font styles liked:
• Please keep in line with Logo

Colors
3277b5

Requirements
Must have
• Site will have 10 pages. Logo must be included.
• Navigation menue will consist of Home, About, Services (with 3 pages in drop down Services offered, Mortgage FAQ and Realotrs), Calculators, Apply Now , Blog and Contact.
• Font should be in line with logo.
Nice to have
• Bright pictures, simplicity, and overall feeling of professionalism/knowledge.

```html
<!DOCTYPE html>
<html lang="en">
<head>
<meta charset="utf-8">
<title>Elmridge Mortgage Group</title>
<link href="https://fonts.googleapis.com/css2?family=Raleway:ital,wght@0,400;0,500;0,600;0,700;1,400&display=swap" rel="stylesheet">
<style>
:root{
  --blue:#3277b5;
  --blue-dark:#2a66a0;
  --green:#5a9e1a;
  --ink:#2f2f2f;
  --text:#555;
  --muted:#888;
  --line:#d8d8d8;
  --grey-band:#eeeeee;
  --panel:#e4e4e4;
  --white:#fff;
}
*{box-sizing:border-box;margin:0;padding:0}
html,body{width:1200px;height:2466px;overflow:hidden}
body{position:relative;background:var(--white);font-family:'Raleway',sans-serif;color:var(--text)}
.abs{position:absolute}
a{color:inherit;text-decoration:none}

/* header */
.brand{left:76px;top:22px;display:flex;align-items:center;gap:10px;color:var(--blue);font-weight:700;font-size:17px;line-height:1.1}
.brand-dot{width:44px;height:44px;border-radius:50%;background:var(--blue)}
.brand.footer-brand{color:var(--white)}
.brand.footer-brand .brand-dot{background:var(--white)}
.phone{left:800px;top:22px;display:flex;align-items:center;gap:10px;color:var(--blue);font-size:18px;font-weight:500}
.btn{display:inline-flex;align-items:center;justify-content:center;background:var(--green);color:var(--white);border-radius:22px;font-weight:500}
.header-apply{left:988px;top:16px;width:138px;height:38px;font-size:17px}
.nav{left:0;top:82px;width:1200px;height:24px}
.nav a{position:absolute;font-size:17px;font-weight:500;color:var(--ink)}
.nav a.active{color:var(--blue)}
.dropdown{left:681px;top:118px;width:180px;height:132px;background:#5d5d5d;box-shadow:0 3px 8px rgba(0,0,0,.35);z-index:5}
.dropdown a{position:absolute;left:16px;color:var(--white);font-size:15px;font-weight:500}
.dropdown a::before{content:"»";margin-right:8px}

/* hero */
.hero{left:0;top:128px;width:1200px;height:510px;background:linear-gradient(180deg,#5f7f80 0%,#8fa39c 45%,#b79a6a 70%,#3b4650 85%,#2b3440 100%)}
.hero-title{left:76px;top:292px;color:var(--white);font-size:28px;font-weight:600;letter-spacing:.3px}
.hero-sub{left:76px;top:336px;width:560px;color:var(--white);font-size:20px;line-height:28px}
.hero-apply{left:76px;top:411px;width:136px;height:38px;font-size:17px}
.dots{display:flex;gap:7px}
.dots span{width:12px;height:12px;border-radius:50%;background:var(--white)}
.dots span.on{background:var(--blue)}
.hero .dots{position:absolute;left:76px;top:425px}

/* calculator */
.calc{left:794px;top:391px;width:332px;height:469px;background:var(--panel);border:3px solid var(--white);box-shadow:0 2px 10px rgba(0,0,0,.35);z-index:4}
.calc-head{height:52px;background:var(--blue);color:var(--white);font-size:22px;font-weight:600;padding:12px 0 0 25px}
.calc label{position:absolute;left:25px;font-size:14px;font-weight:600;color:var(--ink)}
.calc .unit{left:232px}
.slider{position:absolute;left:25px;width:180px;height:3px;background:var(--blue)}
.slider::after{content:"";position:absolute;left:14px;top:-5px;width:13px;height:13px;border-radius:50%;background:var(--blue);border:2px solid var(--white);box-shadow:0 0 0 1px var(--blue)}
.field{position:absolute;left:232px;width:74px;height:30px;background:var(--white);border:1px solid #bbb;font-size:13px;padding:8px 0 0 10px;color:#444}
.select{position:absolute;left:25px;width:281px;height:32px;background:var(--white);border:1px solid #bbb;font-size:13px;color:#777;padding:8px 0 0 14px}
.select::after{content:"⇕";position:absolute;right:12px;top:6px;font-size:14px;color:#444}
.calc-btn{position:absolute;left:25px;width:281px;height:42px;background:linear-gradient(#6a6a6a,#3d3d3d);color:var(--white);font-size:18px;font-weight:600;display:flex;align-items:center;justify-content:center}

/* welcome */
.h2{font-size:24px;font-weight:600;color:var(--blue);letter-spacing:.3px}
.welcome-title{left:76px;top:680px}
.welcome-text{left:76px;top:726px;width:690px;font-size:15px;line-height:25.5px}

/* services band */
.band{left:0;top:894px;width:1200px;height:426px;background:var(--blue)}
.band .h2{color:var(--white);position:absolute;top:38px}
.svc-img{position:absolute;top:92px;width:279px;height:166px}
.svc-title{position:absolute;top:274px;color:var(--white);font-size:21px;font-weight:500}
.svc-text{position:absolute;top:308px;width:270px;color:#dbe7f3;font-size:15px;line-height:25px}
.video{position:absolute;left:709px;top:92px;width:417px;height:280px;border:3px solid #dfe6ee;background:linear-gradient(135deg,#6b6f73,#4a4e52 60%,#8a3b32);box-shadow:0 3px 10px rgba(0,0,0,.3)}
.play{position:absolute;left:179px;top:111px}

/* blog */
.blog-title{left:76px;top:1358px}
.post-img{position:absolute;left:76px;width:151px;height:115px}
.post-head{position:absolute;left:253px;color:var(--blue);font-size:17px;font-weight:600}
.post-meta{position:absolute;left:253px;font-size:12.5px;color:var(--muted)}
.post-text{position:absolute;left:253px;width:410px;font-size:15px;line-height:25px}

/* faq */
.faq-title{left:704px;top:1358px}
.faq{position:absolute;left:704px;width:422px;border:1px solid var(--line);background:var(--white);font-size:15px}
.faq .q{position:absolute;left:17px;top:11px}
.faq .sign{position:absolute;right:14px;top:12px;width:14px;height:14px;border:1px solid #777;font-size:12px;line-height:11px;text-align:center;color:#555}
.faq.open .q{color:var(--blue);font-size:14px}
.faq.open .sign{border-color:var(--blue);color:var(--blue)}
.faq .a{position:absolute;left:17px;top:45px;width:385px;line-height:24px}

/* testimonial */
.clients{left:0;top:1736px;width:1200px;height:317px;background:var(--grey-band);text-align:center}
.clients .h2{position:absolute;left:0;width:1200px;top:38px}
.quote{position:absolute;left:80px;top:92px;width:1040px;font-size:15px;font-style:italic;line-height:26px}
.person{position:absolute;left:0;width:1200px;top:184px;color:var(--blue);font-size:15px;font-weight:600}
.place{position:absolute;left:0;width:1200px;top:209px;color:var(--blue);font-size:13px}
.clients .dots{position:absolute;left:577px;top:260px}
.clients .dots span{width:9px;height:9px;background:#444}

/* press */
.press-title{left:0;width:1200px;top:2088px;text-align:center}
.press{left:0;width:1200px;top:2152px;display:flex;justify-content:center;align-items:center;gap:34px;color:#444;font-size:19px;font-weight:600}

/* footer */
.footer{left:0;top:2228px;width:1200px;height:238px;background:var(--blue);color:var(--white)}
.footer .col{position:absolute;top:36px}
.footer h4{font-size:15px;font-weight:600;margin-bottom:10px;letter-spacing:.3px}
.footer .col a{display:block;font-size:13.5px;line-height:27px}
.copy{position:absolute;left:76px;top:162px;font-size:13.5px;line-height:20px}
.email{position:absolute;left:676px;top:67px;width:228px;height:38px;background:var(--white);color:#666;font-size:13px;padding:12px 0 0 12px}
.signup{position:absolute;left:827px;top:118px;width:77px;height:33px;background:#9d9d9d;border-radius:2px;font-size:13.5px;font-weight:600;display:flex;align-items:center;justify-content:center}
.footer-apply{position:absolute;left:975px;top:37px;width:136px;height:40px;font-size:17px}
</style>
</head>
<body>

<header>
  <div class="brand abs"><span class="brand-dot"></span><span>Elmridge<br>Mortgage Group</span></div>
  <div class="phone abs">
    <svg width="16" height="16" viewBox="0 0 16 16"><rect width="16" height="16" rx="2" fill="#3277b5"/><path d="M5 3.5l2 2-1 1.3c.6 1.3 1.6 2.3 2.9 2.9l1.3-1 2 2-1.2 1.6C7.6 12 4 8.4 3.7 4.7z" fill="#fff"/></svg>
    <span>1-800-555-0142</span>
  </div>
  <a class="btn header-apply abs">Apply Now</a>
  <nav class="nav abs">
    <a style="left:498px">Home</a>
    <a style="left:602px">About</a>
    <a class="active" style="left:705px">Service</a>
    <a style="left:822px">Calculators</a>
    <a style="left:970px">Blog</a>
    <a style="left:1062px">Contact</a>
  </nav>
  <div class="dropdown abs">
    <a style="top:22px">Mortgage</a>
    <a style="top:59px">FAQ</a>
    <a style="top:97px">Realtors</a>
  </div>
</header>

<section class="hero abs" role="img" aria-label="City skyline across the water at dusk">
  <div class="dots"><span class="on"></span><span></span><span></span><span></span></div>
</section>
<h1 class="hero-title abs">WE ARE A MORTGAGE BROKERAGE</h1>
<p class="hero-sub abs">Our firm provides residential and commercial mortgage solutions for clients in Ontario, Canada.</p>
<a class="btn hero-apply abs">Apply Now</a>

<aside class="calc abs">
  <div class="calc-head">CALCULATORS</div>
  <label style="top:70px">Amortization</label><label class="unit" style="top:70px">Years</label>
  <div class="slider" style="top:104px"></div><div class="field" style="top:90px">25</div>
  <label style="top:135px">Payment</label><label class="unit" style="top:135px">$</label>
  <div class="slider" style="top:169px"></div><div class="field" style="top:155px">2,791.70</div>
  <label style="top:200px">Payment Frequency</label>
  <div class="select" style="top:222px">Select</div>
  <label style="top:272px">Product</label>
  <div class="select" style="top:293px">Select</div>
  <label style="top:342px">Interest Rate</label><label class="unit" style="top:342px">%</label>
  <div class="slider" style="top:375px"></div><div class="field" style="top:361px">5.00</div>
  <div class="calc-btn" style="top:404px">CALCULATE</div>
</aside>

<h2 class="h2 welcome-title abs">WELCOME TO OUR WEBSITE</h2>
<p class="welcome-text abs">Aliquam molestie, mi et imperdiet euismod, dui purus auctor tellus, et interdum lacus lectus et ante. Sed accumsan sollicitudin sapien, sit amet adipiscing turpis gravida ac. In congue, neque ac lobortis volutpat, libero mauris varius mi, vitae suscipit ipsum ligula vitae risus. Duis aliquam nibh a dui iaculis viverra id a velit. Vivamus egestas risus in magna varius commodo. Sed semper viverra egestas. Etiam pretium porttitor lectus, vel ornare neque porta volutpat.</p>

<section class="band abs">
  <h2 class="h2" style="left:76px">OUR SERVICES</h2>
  <div class="svc-img" style="left:76px;background:linear-gradient(135deg,#2c3e58,#8a9bb0 60%,#c9b08a)" role="img" aria-label="Handshake over a small house model and documents"></div>
  <div class="svc-title" style="left:76px">Residential Mortgage</div>
  <p class="svc-text" style="left:76px">Vivamus egestas risus in magna varius commodo. Sed semper viverra egestas.</p>
  <div class="svc-img" style="left:391px;background:linear-gradient(180deg,#cfc7b4,#9c8f76 55%,#4e4638)" role="img" aria-label="Cranes over a commercial building under construction"></div>
  <div class="svc-title" style="left:391px">Commercial Mortgage</div>
  <p class="svc-text" style="left:391px">Vivamus egestas risus in magna varius commodo. Sed semper viverra egestas.</p>
  <h2 class="h2" style="left:707px">WATCH A VIDEO</h2>
  <div class="video" role="img" aria-label="Model house resting on a calculator keypad">
    <svg class="play" width="56" height="56" viewBox="0 0 56 56"><circle cx="28" cy="28" r="25" fill="none" stroke="#fff" stroke-width="4"/><path d="M22 17l17 11-17 11z" fill="#fff"/></svg>
  </div>
</section>

<h2 class="h2 blog-title abs">BLOG POSTS</h2>
<div class="post-img" style="top:1407px;background:linear-gradient(135deg,#e9e4dc,#b9a48d 60%,#5a6a80)" role="img" aria-label="Couple meeting with an advisor"></div>
<div class="post-head" style="top:1405px">Aliquam molestie, mi et imperdiet euismod..</div>
<div class="post-meta" style="top:1435px">▣ Apr 07, 2016 &nbsp;|&nbsp; ● By Admin &nbsp;|&nbsp; ▬ 23 Comments</div>
<p class="post-text" style="top:1462px">Sed accumsan sollicitudin sapien, sit amet adipiscing turpis gravida ac. In congue, neque ac lobortis volutpat, libero mauris varius mi..</p>
<div class="post-img" style="top:1562px;background:linear-gradient(135deg,#f1f3f5,#a9b6c4 60%,#3d4a5c)" role="img" aria-label="Calculator and pen on paperwork"></div>
<div class="post-head" style="top:1560px">Aliquam molestie, mi et imperdiet euismod..</div>
<div class="post-meta" style="top:1590px">▣ Apr 07, 2016 &nbsp;|&nbsp; ● By Admin &nbsp;|&nbsp; ▬ 23 Comments</div>
<p class="post-text" style="top:1617px">Sed accumsan sollicitudin sapien, sit amet adipiscing turpis gravida ac. In congue, neque ac lobortis volutpat, libero mauris varius mi..</p>

<h2 class="h2 faq-title abs">FAQ</h2>
<div class="faq" style="top:1407px;height:40px"><span class="q">Aliquam molestie, mi et imperdiet euismod ?</span><span class="sign">+</span></div>
<div class="faq open" style="top:1452px;height:136px"><span class="q">Aliquam molestie, mi et imperdiet euismod ?</span><span class="sign">−</span><p class="a">Sed accumsan sollicitudin sapien, sit amet adipiscing turpis gravida ac. In congue, neque ac lobortis volutpat, libero mauris varius mi..</p></div>
<div class="faq" style="top:1593px;height:40px"><span class="q">Aliquam molestie, mi et imperdiet?</span><span class="sign">+</span></div>
<div class="faq" style="top:1639px;height:40px"><span class="q">Aliquam molestie, mi et imperdiet euismod ?</span><span class="sign">+</span></div>

<section class="clients abs">
  <h2 class="h2">WHAT OUR CLIENTS SAYS</h2>
  <p class="quote">" Sed accumsan sollicitudin sapien, sit amet adipiscing turpis gravida ac. In congue, neque ac lobortis volutpat, libero mauris varius mi, vitae suscipit ipsum ligula vitae risus. Duis aliquam nibh a dui iaculis viverra id a velit. Vivamus egestas risus in magna varius commodo. Sed semper viverra egestas. Etiam pretium porttitor lectus, vel ornare neque porta volutpat."</p>
  <div class="person">-Name Heading</div>
  <div class="place">Location</div>
  <div class="dots"><span></span><span></span><span></span></div>
</section>

<h2 class="h2 press-title abs">AS SEEN ON</h2>
<div class="press abs">
  <span>Harborvale Business Ledger</span>
  <span>Talbery</span>
  <span>Kestrel Four</span>
  <span>Marketwise Report</span>
  <span>Techvane</span>
  <span>Ridgewater Times</span>
</div>

<footer class="footer abs">
  <div class="brand footer-brand abs" style="top:42px"><span class="brand-dot"></span><span>Elmridge<br>Mortgage Group</span></div>
  <p class="copy">Copyright © 2016. All Right Reserved<br>Terms &amp; Conditions</p>
  <div class="col" style="left:363px"><h4>COMPANY</h4><a>Home</a><a>About</a><a>Services</a><a>Calculators</a><a>Blog</a><a>Contact</a></div>
  <div class="col" style="left:529px"><h4>SERVICES</h4><a>Mortgage</a><a>FAQ</a><a>Realtors</a></div>
  <div class="col" style="left:676px"><h4>NEWSLETTER SIGN UP</h4></div>
  <div class="email">Enter Email Address</div>
  <div class="signup">Sign Up</div>
  <a class="btn footer-apply">Apply Now</a>
</footer>

</body>
</html>
```